Banner Ad Design Project for responsive website

Looking to update the main banner on my website www.vowlantern.example but it will be for our new responsive website, you can see here http://www.vowlantern.example/dev/
Banner should be 300 px high by1920 pix wide
Please contact me with any questions
Should include:
All the text from the existing banner ie
Bridal Show
THE FIRST 50 BRIDES WILL GET A CHANCE TO WIN $25000
Honeymoon Cruise Giveaway
"Pick Your Perfect Gown" casting call
Banner should be 1920 pix wide
Final delivery will require layered psd file and all fonts

Target Market(s)

Brides

Industry/Entity Type

Call

Requirements
Must have
• All the text from the existing banner ie
• Bridal Show
• THE FIRST 50 BRIDES WILL GET A CHANCE TO WIN $25000
• Honeymoon Cruise Giveaway
• "Pick Your Perfect Gown" casting call
• Banner should be 1920 pix wide
Nice to have
• The look and feel of our postcard, see attached
Should not have
• Any specifics to any date/time/location as the banner will be online all the time and the specifics for each show will be different

```html
<!DOCTYPE html>
<html lang="en">
<head>
<meta charset="utf-8">
<title>Bridal Show Banner</title>
<link rel="stylesheet" href="https://fonts.googleapis.com/css2?family=Great+Vibes&family=Roboto+Condensed:wght@400;700&family=Open+Sans:wght@400;600&display=swap">
<style>
  :root {
    --stage: #1f1f1f;
    --paper: #f7f7f5;
    --paper-shade: #e7e7e3;
    --green: #1d7a1d;
    --green-dark: #14651a;
    --navy: #24348f;
    --ink: #3a3a3a;
    --rule: #9a9a9a;
    --sky: #5aa8df;
    --sky-light: #a9d3f0;
    --white: #ffffff;
  }
  * { margin: 0; padding: 0; box-sizing: border-box; }
  html, body { width: 1200px; height: 1000px; overflow: hidden; background: var(--stage); }

  /* 1920 x 300 banner scaled to 1152 x 180 */
  .banner {
    position: absolute; left: 24px; top: 410px; width: 1152px; height: 180px;
    overflow: hidden;
    background: radial-gradient(ellipse at 60% 40%, var(--paper) 0%, var(--paper-shade) 100%);
    font-family: "Roboto Condensed", sans-serif;
  }
  .wave { position: absolute; left: 0; top: 0; }
  .couple-photo {
    position: absolute; left: 0; top: 0; width: 230px; height: 180px;
    background: linear-gradient(160deg, #f2f0ec 0%, #e9ddd2 35%, #6e6f74 70%, #f4f4f4 100%);
  }

  /* headline block */
  .bells { position: absolute; top: 20px; width: 44px; height: 32px; background: rgba(29,122,29,0.08); border-radius: 14px; }
  .bells--left { left: 246px; }
  .bells--right { left: 556px; }
  .title {
    position: absolute; left: 292px; width: 262px; top: 8px; text-align: center;
    font-family: "Great Vibes", cursive; font-size: 54px; font-weight: 400; color: var(--green); line-height: 64px;
  }
  .casting {
    position: absolute; left: 240px; width: 362px; top: 84px; text-align: center; white-space: nowrap;
    font-family: "Open Sans", sans-serif; font-size: 16px; color: var(--ink); line-height: 30px;
  }
  .casting .script { font-family: "Great Vibes", cursive; font-size: 24px; color: var(--navy); }

  .rule { position: absolute; top: 14px; height: 112px; border-left: 1px dotted var(--rule); }
  .rule--one { left: 608px; }
  .rule--two { left: 858px; }

  /* prize block */
  .prize-line {
    position: absolute; left: 620px; width: 226px; top: 12px; text-align: center;
    font-size: 15px; line-height: 17px; font-weight: 700; color: var(--ink);
  }
  .prize-amount {
    position: absolute; left: 620px; width: 226px; top: 48px; text-align: center;
    font-size: 40px; font-weight: 700; color: var(--green); line-height: 44px;
  }
  .coupon {
    position: absolute; left: 633px; top: 96px; width: 200px; height: 34px;
    background: var(--green-dark); padding: 3px;
  }
  .coupon-inner {
    height: 100%; border: 1px dashed rgba(255,255,255,0.7);
    display: flex; align-items: center; gap: 5px; padding-left: 6px; color: var(--white);
  }
  .coupon-value { font-size: 22px; font-weight: 700; line-height: 1; }
  .coupon-text { font-size: 11px; line-height: 12px; }

  /* giveaway block */
  .cruise-photo {
    position: absolute; left: 872px; top: 18px; width: 112px; height: 60px;
    border: 2px solid var(--white); border-radius: 3px;
    background: linear-gradient(180deg, #7cc0ee 0%, #cfe8f7 55%, #2f8fc9 100%);
  }
  .giveaway {
    position: absolute; left: 994px; top: 18px; width: 146px; text-align: center;
    font-family: "Great Vibes", cursive; font-size: 24px; line-height: 29px; color: var(--green);
  }

  /* footer on wave */
  .brand {
    position: absolute; left: 244px; top: 152px;
    font-size: 18px; font-weight: 400; line-height: 22px; color: var(--white);
  }
  .sponsor {
    position: absolute; right: 200px; top: 146px; text-align: right;
    color: var(--white); font-size: 11px; font-weight: 700; line-height: 14px;
  }
  .divider { position: absolute; left: 960px; top: 144px; height: 32px; border-left: 1px solid var(--white); }
  .tickets { position: absolute; left: 968px; top: 143px; width: 172px; text-align: right; color: var(--white); }
  .tickets-label { font-size: 12px; line-height: 14px; }
  .tickets-url { font-size: 17px; font-weight: 700; line-height: 20px; }
</style>
</head>
<body>
<main class="banner">
  <svg class="wave" width="1152" height="180" viewBox="0 0 1152 180" aria-hidden="true">
    <path d="M230,136 C520,148 860,150 1152,104 L1152,180 L230,180 Z" fill="var(--sky-light)"/>
    <path d="M230,142 C520,156 860,158 1152,112 L1152,180 L230,180 Z" fill="var(--sky)"/>
  </svg>
  <div class="couple-photo" role="img" aria-label="Photo of a smiling bride in a white gown and veil embracing a groom in a grey suit"></div>

  <div class="bells bells--left" role="img" aria-label="Decorative wedding bells ornament"></div>
  <div class="bells bells--right" role="img" aria-label="Decorative wedding bells ornament"></div>
  <h1 class="title">Bridal Show</h1>
  <p class="casting">Open Casting Call <span class="script">Pick Your Perfect Gown</span></p>

  <div class="rule rule--one"></div>
  <p class="prize-line">THE FIRST 50 BRIDES WILL<br>GET A CHANCE TO WIN</p>
  <p class="prize-amount">$25,000</p>
  <div class="coupon">
    <div class="coupon-inner">
      <span class="coupon-value">$3</span>
      <span class="coupon-text">off admission by<br>using coupon code NP3</span>
    </div>
  </div>

  <div class="rule rule--two"></div>
  <div class="cruise-photo" role="img" aria-label="Photo of a white cruise ship on blue sea"></div>
  <p class="giveaway">Honeymoon<br>Cruise Giveaway</p>

  <p class="brand">Vow Lantern</p>
  <p class="sponsor">Sponsored by<br>Moonlit Melody Entertainment</p>
  <div class="divider"></div>
  <div class="tickets">
    <p class="tickets-label">Get Tickets at</p>
    <p class="tickets-url">vowlantern.example</p>
  </div>
</main>
</body>
</html>
```